Landing Page für Persönlichkeitsquiz
Zielgruppe
Persönlichkeitsquiz für Menschen über 40 Jahren die bessere Entscheidungen treffen möchten.
Aufgabenstellung
Landinpage Design plus QUIZ ( 6 Schritte)
Vollständige Projektbeschreibung:
Projektbeschreibung
„Roaming Sideways QUIZ“
roamingsideways.example
- Responsive Design für mobile & website (Most users: mobile)
- Design wird Grundlage für spätere Website
Dieses Quiz wendet sich an Menschen über 40 Jahre, die ihre persönlichen Lebensziele besser erreichen möchten. Bitte denke daran, dass Menschen in unserem Alter schon schlechter sehen – also bitte eine gut lesbare & etwas größere Schrift verwenden!
Auftrag:
QUIZ mit mehreren Runden
Schritte des Quiz:
1. Landingpage
1.1 Video (youtube eingebunden)
1.2 Text
1.3 „Start Quiz“ Button
1.4 „Bekannt aus“ mit Logos von Medien in denen Marv Olden besprochen wurde.
1.5 Testimonials?
QUIZ (Popup)
2. Erste Runde: „Kille“ alle Antworten die Dich nicht interessieren. Total 64 Antworten.
2.1 Text mit Aufgabenbeschreibung „Kille“ alle Antworten die Dich nicht interessieren. Du hast zwei Minuten.“
2.2 Ein Button pro Antwort (wie bei Lernivo)
2.3 Zwei Buttons pro Reihe
2.4 Oben: Progress bar
2.5 Oben: Countdown clock, Restzeit: 2 Minuten
3. Zweite Runde: „Wähle max. 18 Antworten aus die überleben sollen.“
3.1 Text mit Aufgabenbeschreibung „Wähle max. 18 Antworten aus die überleben sollen.“
3.2 Ein Button pro Antwort (wie bei Lernivo)
3.3 Zwei Buttons pro Reihe
3.4 Oben: Progress bar
3.5 Oben: Countdown clock, Restzeit: 60 Sekunden
3.6 Zähler der noch verfügbaren Antworten. Hier: Noch 18, noch 17, noch 16.. etc.
4. Dritte Runde: „Nur 9 Antworten dürfen überleben. Go!“
4.1 Text mit „Nur 9 Antworten dürfen überleben. Go!“
4.2 Ein Button pro Antwort (wie bei Lernivo)
4.3 Zwei Buttons pro Reihe
4.4 Oben: Progress bar
4.5 Oben: Countdown clock, Restzeit 45 ..

```html
<!DOCTYPE html>
<html lang="de">
<head>
<meta charset="utf-8">
<title>Roaming Sideways Quiz</title>
<link href="https://fonts.googleapis.com/css2?family=Open+Sans:wght@400;600;700&display=swap" rel="stylesheet">
<style>
:root{
  --hero-a:#4b1a9e;
  --hero-b:#2e118a;
  --hero-text:#6f4fc4;
  --press-bg:#663cb8;
  --voices-bg:#5e38ac;
  --card-bg:#6a3fbd;
  --card-edge:#5230a0;
  --ink-dark:#24124f;
  --ink-card:#2b1560;
  --footer-bg:#371590;
  --footer-text:#5f43bb;
  --accent:#c46bd6;
  --gold:#e0a632;
  --gold-dim:#5b2a6a;
  --grey-text:#666;
  --option-bg:#ececec;
  --white:#fff;
}
*{box-sizing:border-box;margin:0;padding:0}
html,body{width:1161px;height:1200px;overflow:hidden}
body{font-family:"Open Sans",sans-serif;position:relative;background:var(--footer-bg)}
.abs{position:absolute}

/* hero */
.hero{left:0;top:0;width:1161px;height:550px;background:linear-gradient(120deg,var(--hero-a),var(--hero-b));overflow:hidden}
.brand{left:84px;top:52px;color:var(--hero-text);font-weight:700;font-size:17px;line-height:23px;letter-spacing:.3px}
.nav{top:80px;color:var(--hero-text);font-size:13.5px}
.nav-lang{left:940px;display:flex;align-items:center;gap:6px}
.nav-questions{left:1035px}
.hero-title{left:84px;top:192px;color:var(--hero-text);font-weight:700;font-size:25px;line-height:34px;white-space:nowrap}
.hero-copy{left:84px;top:275px;color:var(--hero-text);font-size:12.5px;line-height:17px;white-space:nowrap}
.btn-start{background:var(--gold-dim);color:#7a4ad0;font-weight:700;font-size:13px;border-radius:20px;display:flex;align-items:center;justify-content:center;gap:6px;padding:0 14px;white-space:nowrap}
.hero-btn{left:84px;top:350px;height:36px;width:130px;justify-content:flex-start}
.hero-media{left:993px;top:145px;width:83px;height:270px;background:#5b2396}
.hero-dot{left:980px;top:118px;width:38px;height:38px;border-radius:50%;background:#5b2396}

/* modal */
.quiz{left:168px;top:112px;width:825px;height:416px;background:var(--white);border-bottom:4px solid var(--accent);box-shadow:0 6px 20px rgba(20,0,60,.25)}
.step{left:563px;top:94px;width:35px;height:35px;border-radius:50%;background:var(--accent);border:2px solid var(--white);color:var(--white);font-weight:700;font-size:17px;display:flex;align-items:center;justify-content:center}
.back{left:30px;top:22px;color:var(--gold);font-weight:700;font-size:13.5px;display:flex;align-items:center;gap:6px}
.timer{left:298px;top:23px;display:flex;align-items:center;gap:6px;font-size:15px}
.timer-count{color:var(--accent);font-weight:700}
.timer-rest{color:var(--grey-text);border-left:1px solid #ccc;padding-left:4px}
.complete{right:30px;top:23px;color:var(--accent);font-weight:700;font-size:13px}
.progress{left:30px;top:58px;width:765px;height:11px;border-radius:6px;background:var(--option-bg);overflow:hidden}
.progress-fill{width:567px;height:100%;background:var(--accent);border-radius:6px}
.task{left:0;width:825px;text-align:center;color:var(--grey-text)}
.task-title{top:92px;font-weight:700;font-size:20.5px}
.task-sub{top:120px;font-size:14.5px}
.option{width:241px;height:47px;background:var(--option-bg);color:var(--grey-text);font-size:13.5px;display:flex;align-items:center;justify-content:space-between;padding:0 10px;white-space:nowrap}
.option.is-picked{background:var(--accent);color:var(--white)}
.box{width:15px;height:15px;background:var(--white);display:flex;align-items:center;justify-content:center}
.scroll{left:690px;top:146px;width:6px;height:243px;border-radius:3px;background:var(--option-bg)}
.scroll-thumb{left:0;top:80px;width:6px;height:49px;border-radius:3px;background:var(--accent)}
.remaining{left:25px;top:342px;color:var(--grey-text);font-size:12px;line-height:17px}
.remaining strong{color:var(--accent);font-weight:700}
.next{right:30px;top:360px;color:var(--gold);font-weight:700;font-size:13.5px;display:flex;align-items:center;gap:6px}

/* press */
.press{left:0;top:550px;width:1161px;height:254px;background:var(--press-bg);overflow:hidden}
.section-title{left:0;width:1161px;text-align:center;color:var(--ink-dark);font-weight:700;font-size:15px}
.rule{left:561px;width:39px;height:3px;background:#4a2498}
.press-arrow{width:18px;height:18px;border-radius:50%;background:var(--gold-dim);display:flex;align-items:center;justify-content:center}
.outlets{left:125px;top:128px;width:918px;height:30px;display:flex;align-items:center;justify-content:space-between}
.outlet{color:var(--ink-dark);font-weight:700;font-size:17px;display:flex;align-items:center;gap:7px;white-space:nowrap}
.outlet-mark{width:15px;height:15px;background:var(--ink-dark)}
.deco-round{width:170px;height:170px;border-radius:50%;background:#3c1796}

/* voices */
.voices{left:0;top:804px;width:1161px;height:351px;background:var(--voices-bg);overflow:hidden}
.card{top:108px;width:325px;height:153px;background:var(--card-bg);border-bottom:4px solid var(--card-edge)}
.avatar{left:16px;top:17px;width:66px;height:66px;border-radius:50%}
.card-name{left:100px;top:31px;color:var(--ink-card);font-weight:700;font-size:13.5px}
.card-origin{left:100px;top:55px;color:var(--ink-card);font-size:10px}
.card-origin b{font-weight:700}
.card-quote{left:16px;top:92px;width:300px;color:var(--ink-card);font-size:11px;line-height:14.5px}
.card-icon{right:14px;top:11px}
.voices-btn{left:517px;top:290px;height:36px;width:126px}

/* footer */
.footer{left:0;top:1155px;width:1161px;height:45px;color:var(--footer-text);font-size:11px}
.footer span{position:absolute;top:14px}
</style>
</head>
<body>

<section class="abs hero">
  <div class="abs brand">ROAMING<br>SIDEWAYS</div>
  <div class="abs nav nav-lang">Deutsch
    <svg width="12" height="8" viewBox="0 0 12 8"><path d="M1 1l5 5 5-5" fill="none" stroke="#6f4fc4" stroke-width="1.6"/></svg>
  </div>
  <div class="abs nav nav-questions">Fragen</div>
  <h1 class="abs hero-title">Herzlich willkommen<br>bei Roaming Sideways</h1>
  <p class="abs hero-copy">Lorem ipsum dolor sit amet,<br>nonumy eirmod tempor invidunt<br>aliquyam erat, sed diam.</p>
  <div class="abs btn-start hero-btn">
    <svg width="12" height="12" viewBox="0 0 12 12"><path d="M1 6h9M6 2l4 4-4 4" fill="none" stroke="#7a4ad0" stroke-width="1.6"/></svg>Quiz starten
  </div>
  <div class="abs hero-dot"></div>
  <div class="abs hero-media" role="img" aria-label="Vorschaubild des Einführungsvideos"></div>
</section>

<section class="abs quiz">
  <div class="abs back">
    <svg width="18" height="18" viewBox="0 0 18 18"><circle cx="9" cy="9" r="9" fill="#e0a632"/><path d="M10.5 5.5L7 9l3.5 3.5" fill="none" stroke="#fff" stroke-width="1.8"/></svg>zurück
  </div>
  <div class="abs timer">
    <svg width="17" height="17" viewBox="0 0 17 17"><circle cx="8.5" cy="8.5" r="7.5" fill="none" stroke="#c46bd6" stroke-width="1.5"/><path d="M8.5 4v5h3.5" fill="none" stroke="#c46bd6" stroke-width="1.5"/></svg>
    <span class="timer-count">00 : 45</span><span class="timer-rest">Restzeit: 45 Sekunden</span>
  </div>
  <div class="abs complete">50 % komplett</div>
  <div class="abs progress"><div class="progress-fill"></div></div>
  <h2 class="abs task task-title">Nur 9 Antworten dürfen überleben. Go!</h2>
  <p class="abs task task-sub">Du hast 45 Sekunden.</p>

  <div class="abs option is-picked" style="left:167px;top:162px">Lorem ipsum dela martime de.<span class="box"><svg width="11" height="9" viewBox="0 0 11 9"><path d="M1 4.5l3 3 6-6" fill="none" stroke="#c46bd6" stroke-width="2"/></svg></span></div>
  <div class="abs option" style="left:417px;top:162px">Lorem ipsum dela martime de.<span class="box"></span></div>
  <div class="abs option" style="left:167px;top:219px">Lorem ipsum dela martime de.<span class="box"></span></div>
  <div class="abs option is-picked" style="left:417px;top:219px">Lorem ipsum dela martime de.<span class="box"><svg width="11" height="9" viewBox="0 0 11 9"><path d="M1 4.5l3 3 6-6" fill="none" stroke="#c46bd6" stroke-width="2"/></svg></span></div>
  <div class="abs option" style="left:167px;top:275px">Lorem ipsum dela martime de.<span class="box"></span></div>
  <div class="abs option is-picked" style="left:417px;top:275px">Lorem ipsum dela martime de.<span class="box"><svg width="11" height="9" viewBox="0 0 11 9"><path d="M1 4.5l3 3 6-6" fill="none" stroke="#c46bd6" stroke-width="2"/></svg></span></div>
  <div class="abs option is-picked" style="left:167px;top:331px">Lorem ipsum dela martime de.<span class="box"><svg width="11" height="9" viewBox="0 0 11 9"><path d="M1 4.5l3 3 6-6" fill="none" stroke="#c46bd6" stroke-width="2"/></svg></span></div>
  <div class="abs option" style="left:417px;top:331px">Lorem ipsum dela martime de.<span class="box"></span></div>

  <div class="abs scroll"><div class="abs scroll-thumb"></div></div>
  <div class="abs remaining">noch<br><strong>5 auswählen</strong></div>
  <div class="abs next">weiter
    <svg width="18" height="18" viewBox="0 0 18 18"><circle cx="9" cy="9" r="9" fill="#e0a632"/><path d="M7.5 5.5L11 9l-3.5 3.5" fill="none" stroke="#fff" stroke-width="1.8"/></svg>
  </div>
</section>
<div class="abs step">3</div>

<section class="abs press">
  <div class="abs deco-round" style="left:1119px;top:20px"></div>
  <h2 class="abs section-title" style="top:38px">Bekannt aus</h2>
  <div class="abs rule" style="top:66px"></div>
  <div class="abs press-arrow" style="left:84px;top:134px"><svg width="8" height="10" viewBox="0 0 8 10"><path d="M6 1L2 5l4 4" fill="none" stroke="#8a50d0" stroke-width="1.6"/></svg></div>
  <div class="abs outlets">
    <div class="outlet"><span class="outlet-mark"></span>Abendkurier</div>
    <div class="outlet">Le Matin Libre</div>
    <div class="outlet">Nordfunk</div>
    <div class="outlet">Eurowelle</div>
    <div class="outlet">Radio Zwei</div>
    <div class="outlet">Westklang</div>
    <div class="outlet"><span class="outlet-mark"></span>Tagesblick</div>
  </div>
  <div class="abs press-arrow" style="left:1059px;top:134px"><svg width="8" height="10" viewBox="0 0 8 10"><path d="M2 1l4 4-4 4" fill="none" stroke="#8a50d0" stroke-width="1.6"/></svg></div>
</section>

<section class="abs voices">
  <div class="abs deco-round" style="left:-125px;top:50px;background:#4a1fa0"></div>
  <h2 class="abs section-title" style="top:48px">Was sagen andere zum Quiz</h2>
  <div class="abs rule" style="top:75px"></div>

  <article class="abs card" style="left:84px">
    <div class="abs avatar" role="img" aria-label="Porträtfoto von Fatima Mustermann" style="background:radial-gradient(circle at 50% 40%,#6a4a6a,#2f2050)"></div>
    <div class="abs card-name">Fatima Mustermann</div>
    <div class="abs card-origin">aus&nbsp; <b>Berlin</b></div>
    <svg class="abs card-icon" width="20" height="20" viewBox="0 0 20 20"><path d="M10 2a8 7 0 1 1-4.5 12.8L2 17l1.3-4A7 7 0 0 1 10 2z" fill="none" stroke="#4a2498" stroke-width="1.5"/></svg>
    <p class="abs card-quote">Lorem ipsum dolor sit amet, consetetur sadipscing elitr, sed diam nonumy eirmod tempor invidunt ut labore et dolore magna aliquyam erat, sed diam voluptua.</p>
  </article>
  <article class="abs card" style="left:418px">
    <div class="abs avatar" role="img" aria-label="Porträtfoto von James Mustermelian" style="background:radial-gradient(circle at 50% 40%,#5a4250,#2a1d3a)"></div>
    <div class="abs card-name">James Mustermelian</div>
    <div class="abs card-origin">aus&nbsp; <b>Bayern</b></div>
    <svg class="abs card-icon" width="20" height="20" viewBox="0 0 20 20"><path d="M10 2a8 7 0 1 1-4.5 12.8L2 17l1.3-4A7 7 0 0 1 10 2z" fill="none" stroke="#4a2498" stroke-width="1.5"/></svg>
    <p class="abs card-quote">Lorem ipsum dolor sit amet, consetetur sadipscing elitr, sed diam nonumy eirmod tempor invidunt ut labore et dolore magna aliquyam erat, sed diam voluptua.</p>
  </article>
  <article class="abs card" style="left:752px">
    <div class="abs avatar" role="img" aria-label="Porträtfoto von Christiane Weißfuss" style="background:radial-gradient(circle at 50% 40%,#6a5070,#2f2250)"></div>
    <div class="abs card-name">Christiane Weißfuss</div>
    <div class="abs card-origin">aus&nbsp; <b>Hannover</b></div>
    <svg class="abs card-icon" width="20" height="20" viewBox="0 0 20 20"><path d="M10 2a8 7 0 1 1-4.5 12.8L2 17l1.3-4A7 7 0 0 1 10 2z" fill="none" stroke="#4a2498" stroke-width="1.5"/></svg>
    <p class="abs card-quote">Lorem ipsum dolor sit amet, consetetur sadipscing elitr, sed diam nonumy eirmod tempor invidunt ut labore et dolore magna aliquyam erat, sed diam voluptua.</p>
  </article>

  <div class="abs btn-start voices-btn">
    <svg width="12" height="12" viewBox="0 0 12 12"><path d="M1 6h9M6 2l4 4-4 4" fill="none" stroke="#7a4ad0" stroke-width="1.6"/></svg>Quiz starten
  </div>
</section>

<footer class="abs footer">
  <span style="left:84px">© Roaming Sideways QUIZ</span>
  <span style="left:851px">Impressum</span>
  <span style="left:941px">Datenschutz</span>
  <span style="left:1030px">Sitemap</span>
</footer>

</body>
</html>
```